BRPS Postcard Design: Mosquito Control, Lawn Maintenance and Pressure washing

I have a new company based in Atlanta,Georgia named Brookvale Pest Shield Services, LLC. We specializes in Mosquito Control. We also have additional services: Lawn maintenance, Pressure Washing and Gutter Cleaning. I would like to see designs with the colors Black, Red, Gray. We would like the customer to think of us when it comes to Enjoying a mosquito free yard and improving the look and feel of their home and lawn.

Industry/Entity Type

It Company

Requirements
Nice to have
• Treatment plans starting at $69/mt - front of card
• The additional services we offer - back of card.

```html
<!DOCTYPE html>
<html lang="en">
<head>
<meta charset="utf-8">
<title>Brookvale Pest Shield Services – Postcard</title>
<link rel="stylesheet" href="https://fonts.googleapis.com/css2?family=Russo+One&family=Exo+2:ital,wght@1,700&family=Fira+Sans+Condensed:ital,wght@1,600&family=Open+Sans:wght@700&display=swap">
<style>
  :root {
    --black: #231f20;
    --red: #e4222a;
    --white: #ffffff;
    --light: #f4f4f4;
    --mid-gray: #c9c9c9;
    --label-gray: #dedede;
    --text-dark: #1d1b1c;
  }
  * { margin: 0; padding: 0; box-sizing: border-box; }
  html, body { width: 1200px; height: 840px; overflow: hidden; background: var(--white); }
  .postcard { position: relative; width: 1200px; height: 840px; overflow: hidden; }
  .postcard__art { position: absolute; inset: 0; width: 1200px; height: 840px; }

  .brand { position: absolute; left: 0; right: 0; text-align: center; }
  .brand__name {
    top: 50px; font-family: "Russo One", sans-serif; font-size: 108px;
    color: var(--red); line-height: 1; letter-spacing: 1px;
  }
  .brand__tagline {
    top: 176px; font-family: "Exo 2", sans-serif; font-style: italic; font-weight: 700;
    font-size: 46px; color: var(--white); letter-spacing: 2px; line-height: 1;
  }
  .brand__phone {
    top: 244px; font-family: "Russo One", sans-serif; font-size: 78px;
    color: var(--red); letter-spacing: 4px; line-height: 1;
  }

  .services { position: absolute; left: 118px; top: 518px; }
  .services__label {
    display: inline-block; background: var(--label-gray); padding: 4px 14px 6px 40px;
    font-family: "Fira Sans Condensed", sans-serif; font-style: italic; font-weight: 600;
    font-size: 38px; color: var(--red); letter-spacing: 1px; line-height: 1.1;
  }
  .services__list { list-style: none; margin-top: 18px; margin-left: -2px; }
  .services__item {
    display: flex; align-items: center; gap: 14px; height: 59px;
    font-family: "Open Sans", sans-serif; font-weight: 700; font-size: 41px; color: var(--text-dark);
  }
  .services__tick { width: 40px; height: 36px; flex: none; }

  .offer {
    position: absolute; right: 38px; top: 572px; text-align: right;
    font-family: "Open Sans", sans-serif; font-weight: 700;
  }
  .offer__intro { color: var(--red); font-size: 38px; line-height: 58px; }
  .offer__intro span { display: block; }
  .offer__price { color: var(--white); font-size: 92px; line-height: 1; margin-top: 10px; letter-spacing: -1px; }
</style>
</head>
<body>
<main class="postcard">
  <svg class="postcard__art" viewBox="0 0 1200 840" preserveAspectRatio="none" aria-hidden="true">
    <defs>
      <linearGradient id="body-fill" x1="0" y1="0" x2="1" y2="1">
        <stop offset="0" stop-color="#e6e6e6"/>
        <stop offset="0.45" stop-color="#fbfbfb"/>
        <stop offset="1" stop-color="#e9e9e9"/>
      </linearGradient>
      <linearGradient id="silver" x1="0" y1="1" x2="1" y2="0">
        <stop offset="0" stop-color="#8a8a8a"/>
        <stop offset="0.5" stop-color="#e0e0e0"/>
        <stop offset="1" stop-color="#9a9a9a"/>
      </linearGradient>
    </defs>
    <rect class="body-panel" width="1200" height="840" fill="url(#body-fill)"/>
    <rect class="header-panel" width="1200" height="384" fill="var(--black)"/>
    <polygon class="header-shadow" points="0,437 342,437 390,404 1200,404 1200,420 400,420 356,456 0,456" fill="var(--mid-gray)"/>
    <polygon class="header-band" points="0,382 1200,382 1200,404 390,404 342,437 0,437" fill="var(--red)"/>
    <path class="offer-silver" d="M505,840 Q640,560 1200,490 L1200,507 Q720,585 545,840 Z" fill="url(#silver)"/>
    <path class="offer-red-line" d="M500,840 Q635,556 1200,486 L1200,492 Q642,562 508,840 Z" fill="var(--red)"/>
    <path class="offer-panel" d="M540,840 Q716,583 1200,505 L1200,840 Z" fill="var(--black)"/>
  </svg>

  <h1 class="brand brand__name">Brookvale</h1>
  <p class="brand brand__tagline">Pest Shield Services LLC</p>
  <p class="brand brand__phone">404-555-0182</p>

  <section class="services">
    <h2 class="services__label">Additional services:</h2>
    <ul class="services__list">
      <li class="services__item"><svg class="services__tick" viewBox="0 0 40 36"><path d="M2,20 L9,15 L16,24 L35,2 L39,6 L16,34 Z" fill="var(--red)"/></svg>Lawn maintenance</li>
      <li class="services__item"><svg class="services__tick" viewBox="0 0 40 36"><path d="M2,20 L9,15 L16,24 L35,2 L39,6 L16,34 Z" fill="var(--red)"/></svg>Pressure Washing</li>
      <li class="services__item"><svg class="services__tick" viewBox="0 0 40 36"><path d="M2,20 L9,15 L16,24 L35,2 L39,6 L16,34 Z" fill="var(--red)"/></svg>Gutter Cleaning</li>
    </ul>
  </section>

  <section class="offer">
    <p class="offer__intro"><span>Treatment</span><span>plans starting at</span></p>
    <p class="offer__price">$69/mt</p>
  </section>
</main>
</body>
</html>
```